Business card for a Exhibition booth fabrication company

Hi. My company would like to change our corporate name card. We are an events and Exhibition stand builder company. We would like our corporate name card to resonate what we do. I need someone to create something unique that relates to the industry that I am in. The graphic designer should be creative to incorporate the elements of my industry and try to blend in well in the design of the card. Our aim is to ensure that we are unique and our card can look different from our competitors.
Updates

The decision maker was very busy and didnt had time to make this decision

Target Market(s)

Marketing and events manager from all companies

Contact Information for Business Card

The business card should have the following details:
Name
Job Title
Email
Website

Colors

Designer to choose colors to be used in the design.

Requirements
Must have
• The card must be look something that is relevant to the service that I am providing. My website is: www.velmora-buildworks.example
• You can see my website to get more information on what service that I am doing
Nice to have
• On the back of my card, I would like to have a globe image with the incorporation of my company logo. This is to indicate that my services can be done in any part of the world.

```html
<!DOCTYPE html>
<html lang="en">
<head>
<meta charset="utf-8">
<title>Velmora Buildworks – Business Card</title>
<link rel="stylesheet" href="https://fonts.googleapis.com/css2?family=Lato:wght@400;700&family=Montserrat:wght@600;700&display=swap">
<style>
  :root {
    --backdrop: #3a3a3c;
    --card: #262627;
    --card-edge: #1e1e1f;
    --red: #e3222b;
    --red-dark: #a5141b;
    --white: #f4f4f4;
    --rule: #8a8a8a;
    --globe-light: #bdbdbd;
    --globe-dark: #2e2e2f;
  }
  * { margin: 0; padding: 0; box-sizing: border-box; }
  html, body { width: 1200px; height: 900px; overflow: hidden; }
  body {
    background: var(--backdrop);
    font-family: "Lato", sans-serif;
    display: flex;
    flex-direction: column;
    align-items: center;
    justify-content: center;
    gap: 34px;
  }
  .card {
    position: relative;
    width: 700px;
    height: 400px;
    background: var(--card);
    box-shadow: 0 10px 30px rgba(0,0,0,.45);
    overflow: hidden;
  }

  /* Back side */
  .card-back .globe {
    position: absolute;
    left: 190px;
    top: 40px;
    width: 320px;
    height: 320px;
    border-radius: 50%;
    background: radial-gradient(circle at 68% 45%, var(--globe-light) 0%, #7d7d7e 40%, var(--globe-dark) 80%);
  }
  .card-back .brand-name {
    position: absolute;
    left: 0; right: 0;
    top: 183px;
    text-align: center;
    font-family: "Montserrat", sans-serif;
    font-weight: 700;
    font-size: 30px;
    letter-spacing: 3px;
    color: var(--red);
  }

  /* Front side */
  .card-front .brand-name {
    position: absolute;
    right: 48px;
    top: 88px;
    display: flex;
    align-items: center;
    gap: 12px;
    font-family: "Montserrat", sans-serif;
    font-weight: 600;
    font-size: 22px;
    letter-spacing: 2.5px;
    color: var(--white);
  }
  .card-front .brand-dot {
    width: 16px; height: 16px;
    border-radius: 50%;
    background: var(--red);
  }
  .person {
    position: absolute;
    left: 48px;
    top: 150px;
  }
  .person-name {
    font-family: "Montserrat", sans-serif;
    font-weight: 700;
    font-size: 28px;
    letter-spacing: 2px;
    color: var(--red);
    text-transform: uppercase;
  }
  .person-title {
    font-size: 18px;
    color: var(--white);
    margin-top: 2px;
  }
  .divider {
    position: absolute;
    left: 48px;
    right: 48px;
    top: 240px;
    height: 1px;
    background: var(--rule);
  }
  .contact-list {
    position: absolute;
    list-style: none;
    font-size: 17px;
    color: var(--white);
    letter-spacing: .6px;
  }
  .contact-list li {
    display: flex;
    align-items: center;
    gap: 12px;
    margin-bottom: 12px;
  }
  .contact-list svg { width: 15px; height: 15px; fill: var(--red); flex: none; }
  .contact-phones { left: 48px; top: 258px; }
  .contact-online { right: 48px; top: 258px; }
  .accent-band {
    position: absolute;
    left: 0; right: 0; bottom: 0;
    height: 16px;
    background: linear-gradient(90deg, var(--red), var(--red-dark) 45%, var(--red) 70%, var(--red-dark));
  }
</style>
</head>
<body>

  <section class="card card-back">
    <div class="globe" role="img" aria-label="Grey shaded world globe showing the continents"></div>
    <div class="brand-name">VELMORA BUILDWORKS</div>
  </section>

  <section class="card card-front">
    <div class="brand-name"><span class="brand-dot"></span>VELMORA BUILDWORKS</div>

    <div class="person">
      <div class="person-name">Daniel Reyes</div>
      <div class="person-title">Founder &amp; CEO</div>
    </div>

    <div class="divider"></div>

    <ul class="contact-list contact-phones">
      <li>
        <svg viewBox="0 0 24 24" aria-hidden="true"><path d="M6.6 10.8a15.1 15.1 0 0 0 6.6 6.6l2.2-2.2a1 1 0 0 1 1-.25 11.4 11.4 0 0 0 3.6.57 1 1 0 0 1 1 1V20a1 1 0 0 1-1 1A17 17 0 0 1 3 4a1 1 0 0 1 1-1h3.5a1 1 0 0 1 1 1c0 1.25.2 2.45.57 3.57a1 1 0 0 1-.25 1z"/></svg>
        +65 90018824 (Singapore)
      </li>
      <li>
        <svg viewBox="0 0 24 24" aria-hidden="true"><path d="M6.6 10.8a15.1 15.1 0 0 0 6.6 6.6l2.2-2.2a1 1 0 0 1 1-.25 11.4 11.4 0 0 0 3.6.57 1 1 0 0 1 1 1V20a1 1 0 0 1-1 1A17 17 0 0 1 3 4a1 1 0 0 1 1-1h3.5a1 1 0 0 1 1 1c0 1.25.2 2.45.57 3.57a1 1 0 0 1-.25 1z"/></svg>
        +974 70046213 (Qatar)
      </li>
    </ul>

    <ul class="contact-list contact-online">
      <li>
        <svg viewBox="0 0 24 24" aria-hidden="true"><path d="M2 5h20v14H2z M2 5l10 8 10-8" fill="var(--red)" stroke="var(--card)" stroke-width="1.5"/></svg>
        info@velmora-buildworks.example
      </li>
      <li>
        <svg viewBox="0 0 24 24" aria-hidden="true"><circle cx="12" cy="12" r="10" fill="none" stroke="var(--red)" stroke-width="2"/><path d="M2 12h20M12 2c3 3 3 17 0 20M12 2c-3 3-3 17 0 20" fill="none" stroke="var(--red)" stroke-width="1.6"/></svg>
        www.velmora-buildworks.example
      </li>
    </ul>

    <div class="accent-band"></div>
  </section>

</body>
</html>
```